Design us a professional website for a Cannabis Staffing Agency

We already have a logo ready to go, but now we are looking for a few good web designs. We provide staffing for the Cannabis/Marijuana industry. We want a good balance of clean, simple and modern design but also embracing the exciting atmosphere of the Cannabis industry.

Here are examples of our competition, please note that most of these competitors design feel old and dated:

http://qrvworkforcecircle.example/
https://plorvik.example/plorvik-main-page
http://sapphirepathways.example/index.html
http://www.flaxcrew.example/medical-marijuana-staffing-recruiting
http://www.bramblestaffing.example/
www.takenupstaffing.example
www.pearfirst.example

I also would prefer an explanation of why you choose to design it the way you did? What was your thought process or did you use a template?

Requirements
Must have
• About Us Page
• Candidates Page
• Employer Page
• Job Opening Page
• Contact Us Page
Nice to have
• Colors to match the logo, good use of images and design to show the story. Our goal is to show our clients what we are about and not just tell them.

```html
<!DOCTYPE html>
<html lang="en">
<head>
<meta charset="utf-8">
<title>GROVEHIRE – Cannabis Staffing</title>
<link href="https://fonts.googleapis.com/css2?family=Roboto:wght@300;400;500&family=Roboto+Condensed:wght@400;700&display=swap" rel="stylesheet">
<style>
:root{
  --green:#6a9a06;
  --green-dark:#5a8404;
  --green-soft:#8fb33a;
  --grey:#58595b;
  --text:#555;
  --muted:#777;
  --white:#fff;
  --field:#eef1e8;
}
*{box-sizing:border-box;margin:0;padding:0}
html,body{width:936px;height:1200px;overflow:hidden;background:var(--white);font-family:"Roboto",sans-serif;color:var(--text)}
.page{position:relative;width:936px;height:1200px}
.abs{position:absolute}

/* header */
.brand{display:flex;align-items:center;gap:10px}
.brand-dot{border-radius:50%;background:var(--green);flex:none}
.brand-name{font-family:"Roboto",sans-serif;font-weight:400;color:var(--green);letter-spacing:1px;white-space:nowrap}
.site-header .brand{left:26px;top:14px}
.site-header .brand-dot{width:92px;height:92px}
.site-header .brand-name{font-size:50px}
.btn-register{left:769px;top:20px;width:147px;height:42px;border-radius:21px;background:var(--green);color:var(--white);font-size:14px;font-weight:500;display:flex;align-items:center;justify-content:center}
.main-nav a{position:absolute;top:87px;font-size:12px;color:var(--grey);text-decoration:none;letter-spacing:.3px}
.main-nav a.active{color:var(--green)}

/* banner */
.hero{left:0;top:117px;width:936px;height:250px;background:var(--green)}
.hero .brand{position:absolute;left:50%;top:46px;transform:translateX(-50%)}
.hero .brand-dot{width:92px;height:92px;background:var(--white)}
.hero .brand-name{color:var(--white);font-size:50px}
.hero-title{position:absolute;top:155px;width:100%;text-align:center;font-family:"Roboto Condensed",sans-serif;font-weight:700;font-size:38px;color:var(--white)}

.dots{display:flex;gap:10px;align-items:center}
.dots span{width:6px;height:6px;border-radius:50%;background:#c9d9a6}
.dots span.on{width:13px;height:13px;border:2px solid var(--green);background:radial-gradient(var(--green) 35%,transparent 40%)}
.hero-dots{left:432px;top:377px}

/* stats */
.stat{top:404px;width:216px;height:144px;border-radius:3px;background:linear-gradient(160deg,#7ea41e,#9dbc45 60%,#86aa2a);color:var(--white);text-align:center}
.stat-label{position:absolute;left:10px;top:10px;font-size:13px}
.stat-num{position:absolute;top:42px;width:100%;font-family:"Roboto Condensed",sans-serif;font-size:38px;line-height:1}
.stat-unit{position:absolute;top:80px;width:100%;font-size:13px}
.stat-link{position:absolute;top:125px;width:100%;font-size:11px;text-decoration:underline;font-weight:500}

/* testimonials */
.reviews{left:0;top:562px;width:936px;height:375px;background:linear-gradient(135deg,#7d9f2c,#8cad3a 50%,#748f2a)}
.reviews-title{position:absolute;top:68px;width:100%;text-align:center;font-family:"Roboto Condensed",sans-serif;font-weight:400;font-size:30px;color:var(--white)}
.quote{position:absolute;left:240px;top:130px;width:456px;height:114px;background:var(--white);border-radius:3px;padding:22px 30px;text-align:center;font-size:13px;font-weight:300;line-height:24px;color:var(--grey)}
.quote::after{content:"";position:absolute;left:221px;bottom:-8px;border:7px solid transparent;border-top-color:var(--white);border-bottom:0}
.quote-author{position:absolute;top:264px;width:100%;text-align:center;font-size:13px;color:var(--white)}
.arrow{position:absolute;top:178px}
.reviews .dots{position:absolute;left:432px;top:330px}
.reviews .dots span{background:#b8cd85}

/* footer */
.site-footer .brand{left:10px;top:964px;gap:6px;width:196px}
.site-footer .brand-dot{width:52px;height:52px}
.site-footer .brand-name{font-size:22px;letter-spacing:.5px}
.social{display:flex;gap:8px;left:39px;top:1025px}
.social span{width:26px;height:26px;border-radius:50%;background:var(--green)}
.vline{width:1px;top:962px;height:200px;background:#ccc}
.fcol h3{font-family:"Roboto Condensed",sans-serif;font-weight:400;font-size:15px;color:var(--grey);margin-bottom:14px}
.fcol a{display:block;font-size:12px;font-weight:300;color:var(--muted);text-decoration:none;height:28px;white-space:nowrap}
.subscribe{left:720px;top:1006px;width:184px;height:36px;display:flex;border:1px solid var(--green);border-radius:2px;overflow:hidden}
.subscribe span{flex:1;background:var(--field);font-size:12px;color:#888;padding:10px 11px;font-weight:300;white-space:nowrap}
.subscribe b{width:36px;background:var(--green);display:flex;align-items:center;justify-content:center}
.foot-line{left:0;top:1162px;width:936px;height:2px;background:var(--green)}
.copyright{right:21px;top:1183px;font-size:10px;color:var(--muted)}
</style>
</head>
<body>
<div class="page">

  <header class="site-header">
    <div class="brand abs"><span class="brand-dot"></span><span class="brand-name">GROVEHIRE</span></div>
    <div class="btn-register abs">REGISTER / LOGIN</div>
    <nav class="main-nav">
      <a class="active" style="left:480px">HOME</a>
      <a style="left:543px">CANDIDATE</a>
      <a style="left:637px">EMPLOYER</a>
      <a style="left:727px">JOBS</a>
      <a style="left:786px">ABOUT</a>
      <a style="left:853px">CONTACT</a>
    </nav>
  </header>

  <section class="hero abs" role="img" aria-label="Hero banner area">
    <div class="brand"><span class="brand-dot"></span><span class="brand-name">GROVEHIRE</span></div>
    <div class="hero-title">BANNER HERE</div>
  </section>
  <div class="dots hero-dots abs"><span></span><span></span><span class="on"></span><span></span><span></span></div>

  <section class="stats">
    <div class="stat abs" style="left:125px" role="img" aria-label="Photo of a hand holding a phone over a laptop, tinted green">
      <div class="stat-label">Candidates Hired</div><div class="stat-num">3000+</div><div class="stat-unit">candidates</div><div class="stat-link">MORE INFO</div>
    </div>
    <div class="stat abs" style="left:360px" role="img" aria-label="Photo of a hand holding a phone over a laptop, tinted green">
      <div class="stat-label">Companies using GROVEHIRE</div><div class="stat-num">100+</div><div class="stat-unit">companies</div><div class="stat-link">MORE INFO</div>
    </div>
    <div class="stat abs" style="left:595px" role="img" aria-label="Photo of a hand holding a phone over a laptop, tinted green">
      <div class="stat-label">Current Job Openings</div><div class="stat-num">300+</div><div class="stat-unit">jobs</div><div class="stat-link">MORE INFO</div>
    </div>
  </section>

  <section class="reviews abs" role="img" aria-label="Grid of customer portrait photos tinted green">
    <h2 class="reviews-title">7000+ HAPPY CUSTOMERS</h2>
    <svg class="arrow" style="left:206px" width="12" height="20" viewBox="0 0 12 20"><path d="M10 2 2 10l8 8" fill="none" stroke="#fff" stroke-width="2.5"/></svg>
    <div class="quote">Aenean congue pede in nisi tristique interdum. Sed commodo, ipsum ac dignissim ullamcorper, odio nulla venenatis nisi, in porta dolor neque venenatis lacus. Pellentesque fermentum. Mauris sit</div>
    <svg class="arrow" style="left:718px" width="12" height="20" viewBox="0 0 12 20"><path d="M2 2l8 8-8 8" fill="none" stroke="#fff" stroke-width="2.5"/></svg>
    <div class="quote-author">Dana Colvert</div>
    <div class="dots"><span></span><span></span><span class="on" style="border-color:#fff;background:radial-gradient(#fff 35%,transparent 40%)"></span><span></span><span></span></div>
  </section>

  <footer class="site-footer">
    <div class="brand abs"><span class="brand-dot"></span><span class="brand-name">GROVEHIRE</span></div>
    <div class="social abs" aria-label="Social links"><span></span><span></span><span></span><span></span></div>
    <div class="vline abs" style="left:216px"></div>
    <div class="fcol abs" style="left:239px;top:968px"><h3>CANDIDATE</h3><a>Find a Job</a><a>Register / Login</a></div>
    <div class="fcol abs" style="left:400px;top:968px"><h3>EMPLOYER</h3><a style="margin-top:2px">Find Talent</a><a>Register / Login</a><a>Post a Job</a></div>
    <div class="fcol abs" style="left:560px;top:968px"><h3>ABOUT</h3><a style="margin-top:2px">About Company</a><a>Our Partners</a><a>Why GROVEHIRE?</a><a>News</a><a>Feedback</a><a>Contact Us</a></div>
    <div class="vline abs" style="left:696px"></div>
    <div class="fcol abs" style="left:720px;top:968px"><h3>SUBSCRIBE</h3></div>
    <div class="subscribe abs"><span>Enter email address</span><b><svg width="8" height="12" viewBox="0 0 8 12"><path d="M1 1l5 5-5 5" fill="none" stroke="#fff" stroke-width="1.8"/></svg></b></div>
    <div class="foot-line abs"></div>
    <div class="copyright abs">© GROVEHIRE, 2018. All Rights Reserved.</div>
  </footer>

</div>
</body>
</html>
```